Label for Curcumin Supplement

Hi,
We are launching a new dietary supplement derived from curcumin called ZelvaMax.
I have another line of dietary supplements and I want the label for ZelvaMax to be roughly modeled on the label I am attaching but be more modern and sleek looking .

Color Scheme: White and yellowish (like the color of curcumin)
Dimensions: 145mm x 55 mm

Top of Label:
1. Should say ZelvaMax in the same type of text as the example label.

2. ZelvaMax image of a turmeric root, it should be an illustration that is mostly realistic looking, with not too much detail

3. The image of the tumeric root fades away and becomes bubbles that move upper right to show microencapsulation (see my drawing for inspiration). I want this image to show that the supplement is being slowly released. The image would fade away somewhat.

3. Text under the image says “Microencapsulated for extended release” (see drawing for inspiration)

Middle of Label
4. Text should say
“Tumeric Curcumin” (make this big and nice)

5. Information
“ Microencapsulation for controlled release and more bioavailability”
“Peperine and Quercetin for increased absorption”

Bottom of label
6. Should say “Dietary Supplement”
7. 60 Capsules

For now lets focus on the front. The remaining areas of the label please copy the areas in the example label I’ve attached. This will be temporary.

Industry/Entity Type

Supplement

```html
<!DOCTYPE html>
<html lang="en">
<head>
<meta charset="utf-8">
<title>ZelvaMax Tumeric Curcumin Label</title>
<link rel="stylesheet" href="https://fonts.googleapis.com/css2?family=Indie+Flower&family=Open+Sans:wght@400;700;800&display=swap">
<style>
  :root {
    --curcumin: #f9cf10;
    --curcumin-deep: #f2c200;
    --white: #ffffff;
    --root-brown: #4a2a0d;
    --ink: #2b1a0a;
    --root-light: #d9a066;
    --root-mid: #b7652a;
  }
  * { margin: 0; padding: 0; box-sizing: border-box; }
  html, body { width: 1200px; height: 462px; overflow: hidden; background: var(--white); }
  .label {
    position: relative;
    width: 1200px;
    height: 462px;
    font-family: "Open Sans", sans-serif;
    color: var(--ink);
  }
  .label-frame { position: absolute; inset: 0; }
  .brand-panel {
    position: absolute;
    left: 450px; top: 0;
    width: 316px; height: 258px;
  }
  .brand-name {
    position: absolute;
    left: 450px; top: 24px; width: 316px;
    text-align: center;
    font-family: "Indie Flower", cursive;
    font-size: 64px; line-height: 1;
    color: var(--root-brown);
  }
  .root-illustration {
    position: absolute;
    left: 472px; top: 108px;
    width: 272px; height: 140px;
    border-radius: 40px 40px 10px 10px;
    background:
      radial-gradient(ellipse at 80% 10%, rgba(233,196,140,0.55), rgba(255,255,255,0) 45%),
      radial-gradient(ellipse at 40% 75%, var(--root-mid), rgba(183,101,42,0.6) 50%, rgba(255,255,255,0) 75%);
  }
  .release-line {
    position: absolute;
    left: 0; top: 258px; width: 1200px;
    text-align: center;
    font-family: "Indie Flower", cursive;
    color: var(--root-brown);
    font-size: 27px; line-height: 1;
  }
  .release-line .release-small { font-size: 19px; }
  .product-name {
    position: absolute;
    left: 0; top: 280px; width: 1200px;
    text-align: center;
    font-family: "Indie Flower", cursive;
    font-size: 66px; line-height: 1;
    color: var(--root-brown);
  }
  .category-ribbon {
    position: absolute;
    left: 0; top: 353px; width: 1200px;
    text-align: center;
    font-weight: 800; font-size: 18px; letter-spacing: 0.3px;
    color: var(--root-brown);
  }
  .capsule-count {
    position: absolute;
    left: 0; top: 382px; width: 1200px;
    text-align: center;
    font-weight: 700; font-size: 17px;
    color: var(--root-brown);
  }
  .benefit-strip {
    position: absolute;
    left: 0; top: 411px; width: 1200px;
    text-align: center;
    font-size: 16px;
    color: var(--ink);
  }
</style>
</head>
<body>
<div class="label">
  <svg class="label-frame" width="1200" height="462" viewBox="0 0 1200 462" aria-hidden="true">
    <rect x="14" y="8" width="1172" height="444" rx="28" fill="var(--curcumin)"/>
    <rect x="20" y="14" width="1160" height="432" rx="24" fill="none" stroke="var(--white)" stroke-width="2"/>
    <rect x="14" y="408" width="1172" height="26" fill="var(--white)"/>
    <path d="M450 0 V240 Q450 258 468 258 H748 Q766 258 766 240 V0 Z" fill="var(--white)"/>
    <path d="M458 0 V236 Q458 250 472 250 H744 Q758 250 758 236 V0" fill="none" stroke="var(--curcumin)" stroke-width="2"/>
    <path d="M464 0 V232 Q464 244 476 244 H740 Q752 244 752 232 V0" fill="none" stroke="var(--curcumin)" stroke-width="1.5"/>
    <polygon points="420,350 805,350 783,376 442,376" fill="var(--white)"/>
  </svg>

  <div class="brand-name">ZelvaMax</div>
  <div class="root-illustration" role="img" aria-label="Illustration of turmeric roots dissolving into bubbles drifting up to the right"></div>
  <div class="brand-panel"></div>

  <p class="release-line">Microencapsulated <span class="release-small">for extended release</span></p>
  <h1 class="product-name">Tumeric Curcumin</h1>
  <p class="category-ribbon">DIETARY SUPPLEMENT</p>
  <p class="capsule-count">60 Capsules</p>
  <p class="benefit-strip">Microencapsulation for controlled release and more bioavailability, Peperine and Quercetin for increased absorption</p>
</div>
</body>
</html>
```